Design a cool print brochure for an NGO / Give your work a global impact!!

Hi,
I provide a full design brief (below, please scroll) and a mood board (attached) to help you visualize inside my head.. ;-)
I am also available to help and have worked many years in advertising; we will understand each other.
Objective:
To design an A4 folded in two presentation brochure for a non-profit consulting agency called Vantriq.
Vantriq works in sustainability and international development = working with NGO’s, governments and private sector on global issues such as global warming, education for all etc.
Strategy:
This document is a first step in developing a communication strategy. It will be distributed during a major international event called the Meridale Outreach Forum.
Objective:
The double objective of the brochure is:
a) to inform the recipient of what Vantriq is, in the shortest time possible.
b) to showcase relevant projects to demonstrate Vantriq experience and expertise.
Target:
Main target:
Existing Vantriq contacts, such as members of development organizations, NGOs, private sector foundations (CSR), regional networks and other development actors.
NB: the main target already has a certain awareness of Vantriq: we will try to minimize text to maximize visual impact and readability.
Secondary target:
Vantriq will also distribute the brochure to new prospects of interest during the Meridale Forum.
Timing:
We will need to finalize the design and have the files by June 1st to allow time for print before the event.
Content:
The document should be concise, highly readable (no clutter) and include:
1. text (that we will provide)
and
2. visual elements such as images, shapes and info-graphics (that is you).
NB: Vantriq does not have its own image bank; photos will be provided by you.
Format:
A4 folded in half - 4pp A5 - PORTRAIT FORMAT) with an impactful visual in the front, logo, title and headline (please see examples in the mood board attached).
Design elements:
Vantriq does not have yet a visual identity (please see: http://vantriq.org) so there is room for creativity and no graphic chart to follow.
The sector of consulting in international development is rather conservative but our intention is to be disruptive and create a “Wow” effect. We count on you for that!
Therefore, the design should be “structured”, “organized”, “uncluttered” but also “modern”, “impactful”, “highly visual” (think infographic or mind map to describe our services and projects).
Please, take the time to see the attached presentation: I give you guidelines and examples of what we want and what we like.
We are looking forward to seeing your work and I am available for comments, questions and support.
Thank you.
RK
Target Market(s)
The full brief is in the project description: please, scroll through it.
The target market is : our existing clients base, working in sustainable development (read: NGO and Allied Assembly people)
Industry/Entity Type
Ngo
Font styles to use
Requirements
Must have
- - Design and color elements: please, no black and white. Our company website is in black and white and without graphics; we want the brochure to break away from that and start creating our brand identity; so please, show us colors and desing elements (shapes, backgrounds, etc).
- You have a chance to showcase your talent in terms of visual identity: what lines, forms, layout and colors can you come up with and apply throughout the brochure and serve as the visual identity of Vantriq?
- The structure of the document should be:
- - Front cover: design elements + impacful photo (see mood board example attached) +our logo + this headline: "Collective action for sustainable development and impact"
- - Inside front: a graphic representation of "Our Services": such as core activity in the center circle and satellite circles for the services we offer.
- - Inside back:
- 1. Icons and text boxes for "Our projects"
- 2. A world map of the countries where we have worked. Full list of countries is here:
- http://vantriq.org/experience-1
- - Back cover: our contact + logos of partners.
- Our partners are listed here:
- Please use their original logos (ie, in color).
- The design we will select will serve as a basis for a graphic chart...so more work to come...word to the wise ;)
- Please check out our website vantriq.org to see what we do etc.
Nice to have
- Icons to reflect our services: what icons can you come up with to describe "training services", "building networks" or "program management"?
- I give examples in the mood board.
Should not have
- We are open to creativity and want to generate a "Wow" effect.
- Just note that the sector is rather conservative so flashy colors and cartoon like characters should be avoided. Think "earth, global change, Allied Assembly, climate" without going too green (it's overdone). ;-)
- Make us stand out in the NGO world
- Now you.

```html
<!DOCTYPE html>
<html lang="en">
<head>
<meta charset="utf-8">
<title>Vantriq Brochure – Inside Spread</title>
<link href="https://fonts.googleapis.com/css2?family=Comfortaa:wght@500;700&family=Montserrat:wght@400;500;600;700&display=swap" rel="stylesheet">
<style>
  :root{
    --navy:#173a85;
    --blue:#2f5fae;
    --blue-light:#4a78bf;
    --ink:#3a3d44;
    --grey-stripe:#4a4d55;
    --paper:#f4f4f5;
    --stage:#e2e3e5;
    --yellow:#f4c20d;
    --orange:#f39a12;
    --pink:#e5407a;
    --sky:#1f9fd8;
    --green:#23a56b;
    --purple:#8e2a8c;
    --red:#e5462f;
    --label:#dfe7f5;
  }
  *{box-sizing:border-box;margin:0;padding:0}
  html,body{width:1200px;height:833px;overflow:hidden}
  body{background:var(--stage);font-family:"Montserrat",sans-serif;position:relative}
  .spread{position:absolute;left:60px;top:34px;width:1080px;height:764px;display:flex;box-shadow:0 6px 24px rgba(0,0,0,.18)}
  .page{position:relative;width:540px;height:764px;overflow:hidden}

  /* Services page */
  .page--services{background:linear-gradient(135deg,var(--navy) 0%,var(--blue) 65%,var(--blue-light) 100%)}
  .page-base{position:absolute;inset:0}
  .page-title{font-family:"Comfortaa",sans-serif;font-weight:700;font-size:30px;text-align:center;position:absolute;left:0;right:0}
  .page--services .page-title{top:40px;color:#fff}
  .title-rule{position:absolute;left:50%;width:70px;height:3px;transform:translateX(-50%)}
  .page--services .title-rule{top:84px;background:#fff}
  .services-intro{position:absolute;top:104px;left:58px;right:58px;color:#e8eefb;font-size:9px;line-height:1.55;text-align:center}
  .service-map{position:absolute;left:0;top:240px}
  .service-label{font-family:"Montserrat",sans-serif;font-size:10px;fill:var(--label)}
  .core-text{font-family:"Montserrat",sans-serif;font-size:10.5px;font-weight:700;fill:#1b2a4a}

  /* Projects page */
  .page--projects{background:var(--paper)}
  .page--projects .page-title{top:48px;color:var(--ink)}
  .page--projects .title-rule{top:92px;background:var(--ink)}
  .project{position:absolute;width:200px;font-size:10px;line-height:1.35;color:#55585f;text-align:center}
  .project-icon{display:block;margin:0 auto 6px}
  .world-map{position:absolute;left:70px;top:410px;width:400px;height:190px;border-radius:40px 70px 60px 30px;background:radial-gradient(ellipse at 50% 45%,#6e7077 0%,#9a9ca1 60%,rgba(154,156,161,0) 100%)}
  .regions{position:absolute;top:610px;left:40px;right:40px;display:grid;grid-template-columns:1fr 1fr;column-gap:34px;row-gap:10px;font-size:10px;line-height:1.4;color:var(--ink)}
  .region-name{color:var(--blue);font-weight:700}
</style>
</head>
<body>
<div class="spread">

  <section class="page page--services">
    <svg class="page-base" width="540" height="764" viewBox="0 0 540 764" aria-hidden="true">
      <polygon points="0,690 540,660 540,764 0,764" fill="#fff"/>
      <polygon points="0,700 540,670 540,680 0,710" fill="var(--grey-stripe)"/>
    </svg>

    <h2 class="page-title">Our Services</h2>
    <div class="title-rule"></div>
    <p class="services-intro">Vantriq specializes in the analysis of multi-actor cooperation and the facilitation of processes of change. We believe in the need to improve both the understanding and use of collaborative action. For that, we support value-oriented organisations to integrate a better cooperation logic in their daily practice, whether as part of the internal management process or in the context of their relations with other stakeholders. We see our clients as our most important partners. Through them we learn and improve our knowledge about the challenges of collaborative action. That's why listening carefully to our clients' needs and views is a critical step before designing our interventions. We avoid prefabricated solutions. On the contrary, we engage with them in order to find the right solutions that respond to the needs of the organisation and the requirements of each assignment.</p>

    <svg class="service-map" width="540" height="430" viewBox="0 0 540 430" role="img" aria-label="Service areas around the core activity">
      <g stroke="#cfd9ee" stroke-width="1.2" stroke-dasharray="4 4" fill="none">
        <line x1="270" y1="200" x2="210" y2="80"/>
        <line x1="270" y1="200" x2="425" y2="140"/>
        <line x1="270" y1="200" x2="115" y2="200"/>
        <line x1="270" y1="200" x2="430" y2="265"/>
        <line x1="270" y1="200" x2="105" y2="320"/>
        <line x1="270" y1="200" x2="350" y2="355"/>
      </g>
      <circle cx="270" cy="200" r="80" fill="none" stroke="#fff" stroke-width="2"/>
      <circle cx="270" cy="200" r="72" fill="var(--yellow)"/>
      <text class="core-text" text-anchor="middle">
        <tspan x="270" y="172">Our work encompasses</tspan>
        <tspan x="270" y="186">specific projects and/or</tspan>
        <tspan x="270" y="200">an organisation as a</tspan>
        <tspan x="270" y="214">whole. We do so</tspan>
        <tspan x="270" y="228">through the following</tspan>
        <tspan x="270" y="242">areas of work:</tspan>
      </text>

      <g>
        <circle cx="210" cy="80" r="34" fill="none" stroke="var(--orange)" stroke-width="2"/>
        <circle cx="210" cy="80" r="28" fill="var(--orange)"/>
        <circle cx="210" cy="80" r="20" fill="none" stroke="#fff" stroke-width="1.5"/>
        <text class="service-label" text-anchor="middle"><tspan x="130" y="128">Research and Analysis of</tspan><tspan x="130" y="141">Cooperation Schemes</tspan></text>
      </g>
      <g>
        <circle cx="425" cy="140" r="34" fill="none" stroke="var(--pink)" stroke-width="2"/>
        <circle cx="425" cy="140" r="28" fill="var(--pink)"/>
        <circle cx="425" cy="140" r="20" fill="none" stroke="#fff" stroke-width="1.5"/>
        <text class="service-label" text-anchor="middle"><tspan x="420" y="192">Training To Improve</tspan><tspan x="420" y="205">Networked Action</tspan></text>
      </g>
      <g>
        <circle cx="115" cy="200" r="34" fill="none" stroke="var(--sky)" stroke-width="2"/>
        <circle cx="115" cy="200" r="28" fill="var(--sky)"/>
        <circle cx="115" cy="200" r="20" fill="none" stroke="#fff" stroke-width="1.5"/>
        <text class="service-label" text-anchor="middle"><tspan x="105" y="252">Facilitation Of Processes</tspan><tspan x="105" y="265">Of Change</tspan></text>
      </g>
      <g>
        <circle cx="430" cy="265" r="34" fill="none" stroke="var(--green)" stroke-width="2"/>
        <circle cx="430" cy="265" r="28" fill="var(--green)"/>
        <circle cx="430" cy="265" r="20" fill="none" stroke="#fff" stroke-width="1.5"/>
        <text class="service-label" text-anchor="middle"><tspan x="430" y="316">Evaluation of Multi-actor</tspan><tspan x="430" y="329">Projects and Programs</tspan></text>
      </g>
      <g>
        <circle cx="105" cy="320" r="34" fill="none" stroke="var(--purple)" stroke-width="2"/>
        <circle cx="105" cy="320" r="28" fill="var(--purple)"/>
        <circle cx="105" cy="320" r="20" fill="none" stroke="#fff" stroke-width="1.5"/>
        <text class="service-label" text-anchor="middle"><tspan x="100" y="372">Methodologies for</tspan><tspan x="100" y="385">Organizational Change</tspan><tspan x="100" y="398">and Consensus Building</tspan></text>
      </g>
      <g>
        <circle cx="350" cy="355" r="34" fill="none" stroke="var(--red)" stroke-width="2"/>
        <circle cx="350" cy="355" r="28" fill="var(--red)"/>
        <circle cx="350" cy="355" r="20" fill="none" stroke="#fff" stroke-width="1.5"/>
        <text class="service-label" text-anchor="middle"><tspan x="440" y="400">Coalition Building to</tspan><tspan x="440" y="413">Achieve Collective Goals</tspan></text>
      </g>
    </svg>
  </section>

  <section class="page page--projects">
    <svg class="page-base" width="540" height="764" viewBox="0 0 540 764" aria-hidden="true">
      <polygon points="0,0 120,0 0,330" fill="var(--navy)"/>
      <polygon points="0,345 14,345 0,385" fill="var(--grey-stripe)"/>
      <polygon points="540,360 540,560 455,560" fill="var(--navy)"/>
      <polygon points="540,335 540,348 446,572 432,572" fill="var(--grey-stripe)"/>
    </svg>

    <h2 class="page-title">Our Projects</h2>
    <div class="title-rule"></div>

    <div class="project" style="left:70px;top:125px">
      <svg class="project-icon" width="34" height="34" viewBox="0 0 34 34" aria-hidden="true"><rect x="5" y="4" width="24" height="26" rx="2" fill="none" stroke="var(--blue)" stroke-width="1.6"/><path d="M10 12h14M10 17h14M10 22h9" stroke="var(--blue)" stroke-width="1.6"/></svg>
      Lorem ipsum dolor sit amet, consectetur adipiscing elit, sed do eiusmod tempor incididunt ut labore et dolore magna aliqua.
    </div>
    <div class="project" style="left:290px;top:170px">
      <svg class="project-icon" width="34" height="34" viewBox="0 0 34 34" aria-hidden="true"><rect x="5" y="4" width="24" height="26" rx="2" fill="none" stroke="var(--blue)" stroke-width="1.6"/><path d="M10 12h14M10 17h14M10 22h9" stroke="var(--blue)" stroke-width="1.6"/></svg>
      Lorem ipsum dolor sit amet, consectetur adipiscing elit, sed do eiusmod tempor incididunt ut labore et dolore magna aliqua.
    </div>
    <div class="project" style="left:50px;top:230px">
      <svg class="project-icon" width="34" height="34" viewBox="0 0 34 34" aria-hidden="true"><circle cx="15" cy="15" r="9" fill="none" stroke="var(--blue)" stroke-width="1.6"/><path d="M22 22l8 8" stroke="var(--blue)" stroke-width="2"/></svg>
      Lorem ipsum dolor sit amet, consectetur adipiscing elit, sed do eiusmod tempor incididunt ut labore et dolore magna aliqua.
    </div>
    <div class="project" style="left:280px;top:275px">
      <svg class="project-icon" width="34" height="34" viewBox="0 0 34 34" aria-hidden="true"><rect x="4" y="6" width="26" height="22" rx="2" fill="none" stroke="var(--blue)" stroke-width="1.6"/><path d="M9 13l3 3 5-6M20 13h6M9 22h17" stroke="var(--blue)" stroke-width="1.6" fill="none"/></svg>
      Lorem ipsum dolor sit amet, consectetur adipiscing elit, sed do eiusmod tempor incididunt ut labore et dolore magna aliqua.
    </div>

    <div class="world-map" role="img" aria-label="World map in grey showing the regions where projects have taken place"></div>

    <div class="regions">
      <p><span class="region-name">Europe:</span> EU 28, Norway, Switzerland, Turkey, Montenegro, Ukraine, Serbia, Moldova, Armenia, Georgia and Belarus.</p>
      <p style="padding-top:40px"><span class="region-name">Asia:</span> China, Vietnam, Thailand, Indonesia, Malaysia, Singapore, Bangladesh, Kyrgyzstan, Kazakhstan and Myanmar.</p>
      <p><span class="region-name">America:</span> US, Canada, Guatemala, El Salvador, Panamá, Costa Rica, Honduras, Colombia, Perú, Bolivia, Brazil, Argentina, Uruguay and Paraguay.</p>
      <p><span class="region-name">Africa:</span> South Africa, Mozambique, Ethiopia, Kenya, Uganda, Benin, Senegal, Zimbabwe, Ghana, Tunisia, Egypt and Libya.</p>
    </div>
  </section>

</div>
</body>
</html>
```